Fiber Optic Internet flyer promotion Winter 2016-2017

I am looking for a marketing flyer that will not be folded, single sided that will advertise a Fiber Optic internet promotion that we are currently running.

The design should be clean, flow well, quickly grab attention, and if a very few short seconds list what the promotion is, and direct them to contact us.

It needs to list a few features of the promotion, but does not need to be in this order and should flow well with the flyer
1.) Fiber Optic Internet
2.) 100 Mbits for $140 /month or 150 Mbits for $190 /month
3.) Free construction cost up to $10,000, limited funds available.
4.) Limited time offer. Must commit before funds run out.

(555) 274-3916, www.kelvoranet.example

Target Market(s)

Small to large business

Industry/Entity Type

Internet Service Provider

Requirements
Must have
• Eye catching appeal. Quickly convey the message of the promotion and our company name and phone number.
Should not have
• Our company is primarily a wireless ISP. This promotion is all about Fiber Optic. I do not want to draw attention to the "wireless" portion of our business with this flyer.

```html
<!DOCTYPE html>
<html lang="en">
<head>
<meta charset="utf-8">
<title>Fiber Optic Internet Promotion Flyer</title>
<link rel="stylesheet" href="https://fonts.googleapis.com/css2?family=Archivo+Black&family=Arimo:wght@400;700&display=swap">
<style>
  :root {
    --navy: #14267a;
    --royal: #1f3fa8;
    --red: #d4202f;
    --sky-top: #cfe6fb;
    --sky-mid: #8ec6f2;
    --sky-deep: #4fa2e3;
    --photo-dark: #0b1a3d;
    --photo-mid: #27408f;
    --photo-glow: #7a4fb8;
    --white: #ffffff;
    --page-bg: #e6e7ea;
  }
  * { box-sizing: border-box; margin: 0; padding: 0; }
  html, body { width: 1200px; height: 870px; overflow: hidden; }
  body {
    background: var(--page-bg);
    font-family: "Arimo", Arial, sans-serif;
    position: relative;
  }
  .flyer {
    position: absolute;
    left: 310px; top: 25px;
    width: 580px; height: 820px;
    background: linear-gradient(180deg, var(--sky-top) 0%, var(--sky-mid) 60%, var(--sky-deep) 100%);
    overflow: hidden;
    box-shadow: 0 6px 24px rgba(0,0,0,.18);
  }
  .flyer-shapes { position: absolute; inset: 0; }
  .headline {
    position: absolute; left: 0; top: 118px;
    width: 290px; padding: 10px 0 10px 34px;
    background: rgba(20, 24, 40, .78);
    color: var(--white);
    font-family: "Archivo Black", "Arial Black", sans-serif;
    font-size: 30px; line-height: 1.02; letter-spacing: .5px;
  }
  .price-tag {
    position: absolute;
    border-radius: 50%;
    overflow: hidden;
    border: 5px solid var(--sky-top);
    box-shadow: 0 4px 12px rgba(0,0,60,.3);
    text-align: center;
    color: var(--white);
    font-family: "Archivo Black", "Arial Black", sans-serif;
  }
  .price-tag .tag-top {
    background: linear-gradient(180deg, #6fb3ea, #3b86cf);
    height: 48%;
    display: flex; flex-direction: column; justify-content: flex-end;
    padding-bottom: 4px;
  }
  .price-tag .tag-bottom {
    background: var(--red);
    height: 52%;
    padding-top: 2px;
  }
  .price-tag .speed { line-height: 1; }
  .price-tag .speed-unit { line-height: 1; }
  .price-tag .amount { line-height: .95; }
  .price-tag .per-month { font-family: "Arimo", Arial, sans-serif; font-weight: 700; line-height: 1; }
  .tag-upper { left: 332px; top: 295px; width: 196px; height: 196px; }
  .tag-upper .speed { font-size: 40px; }
  .tag-upper .speed-unit { font-size: 26px; }
  .tag-upper .amount { font-size: 58px; }
  .tag-upper .per-month { font-size: 15px; }
  .tag-lower { left: 72px; top: 442px; width: 236px; height: 236px; }
  .tag-lower .speed { font-size: 48px; }
  .tag-lower .speed-unit { font-size: 31px; }
  .tag-lower .amount { font-size: 70px; }
  .tag-lower .per-month { font-size: 17px; }
  .construction-note {
    position: absolute; left: 350px; top: 548px; width: 220px;
    color: var(--white); font-weight: 700; font-size: 17px; line-height: 1.25;
  }
  .phone {
    position: absolute; right: 22px; top: 642px;
    color: var(--red);
    font-family: "Archivo Black", "Arial Black", sans-serif;
    font-size: 30px; white-space: nowrap;
  }
  .offer {
    position: absolute; left: 34px; top: 686px; width: 260px;
    font-weight: 700; font-size: 18px; line-height: 1.12; color: var(--navy);
  }
  .offer span { display: block; white-space: nowrap; }
  .offer .offer-lead { color: var(--red); }
  .footer {
    position: absolute; left: 0; bottom: 0; width: 100%; height: 66px;
    background: var(--navy);
    display: flex; align-items: center; justify-content: space-between;
    padding: 0 26px;
  }
  .brand { display: flex; align-items: center; gap: 10px; color: var(--white); font-family: "Archivo Black", "Arial Black", sans-serif; font-size: 21px; letter-spacing: 1px; }
  .brand-dot { width: 18px; height: 18px; border-radius: 50%; background: var(--red); }
  .website { color: var(--white); font-weight: 700; font-size: 16px; }
</style>
</head>
<body>
  <article class="flyer">
    <svg class="flyer-shapes" width="580" height="820" viewBox="0 0 580 820">
      <defs>
        <linearGradient id="fiber-glow" x1="0" y1="0" x2="1" y2="1">
          <stop offset="0" stop-color="var(--photo-dark)"/>
          <stop offset=".45" stop-color="var(--photo-glow)"/>
          <stop offset=".75" stop-color="var(--photo-mid)"/>
          <stop offset="1" stop-color="#3aa0e0"/>
        </linearGradient>
      </defs>
      <path class="wedge-red" d="M430 245 C 490 250, 545 270, 580 305 L580 100 L430 100 Z" fill="var(--red)"/>
      <path class="fiber-photo" role="img" aria-label="Photo of glowing fiber optic strands with a network cable plug"
            d="M0 0 H580 V130 C 470 180, 390 320, 270 395 C 180 448, 90 462, 0 455 Z" fill="url(#fiber-glow)"/>
      <path class="wave-line" d="M580 130 C 470 180, 390 320, 270 395 C 180 448, 90 462, 0 455"
            fill="none" stroke="var(--royal)" stroke-width="8"/>
      <line class="tag-string" x1="395" y1="255" x2="425" y2="298" stroke="var(--red)" stroke-width="2"/>
      <line class="tag-string" x1="165" y1="400" x2="190" y2="445" stroke="var(--red)" stroke-width="2"/>
      <path class="construction-band" d="M340 530 H580 V625 H315 Z" fill="var(--navy)"/>
    </svg>

    <h1 class="headline">FIBER OPTIC<br>INTERNET</h1>

    <div class="price-tag tag-upper">
      <div class="tag-top"><span class="speed">150</span><span class="speed-unit">Mbits for</span></div>
      <div class="tag-bottom"><div class="amount">$190</div><div class="per-month">per month</div></div>
    </div>

    <div class="price-tag tag-lower">
      <div class="tag-top"><span class="speed">100</span><span class="speed-unit">Mbits for</span></div>
      <div class="tag-bottom"><div class="amount">$140</div><div class="per-month">per month</div></div>
    </div>

    <p class="construction-note">Free construction cost up to $10,000, limited funds available</p>

    <p class="phone">(555) 274-3916</p>

    <p class="offer"><span class="offer-lead">Limited time offer.</span><span>Must commit before</span><span>funds run out.</span></p>

    <footer class="footer">
      <div class="brand"><span class="brand-dot"></span>KELVORA NETWORKS</div>
      <span class="website">www.kelvoranet.example</span>
    </footer>
  </article>
</body>
</html>
```